Customizable Gift Note Card Design

I need a gift note card designed for my Healthy Snacks Care Package company. I need to be able to customize each card with the customer's gift message to the recipient and print to a standard printer.

The card should be single-sided 5 x 7, include our logo, keep colors and graphics simple since they will be printed for each individual order on a standard printer. I would like the following quote to be included in a small and subtle way: "Food is symbolic of love when words are inadequate." —Brent K. Hollister. Our website themerrypantrybites.com should also be included.

I have included pictures of our product packaging for reference.

Target Market(s)

Gift recipients: Students, people recovering from illness, housewarming, thank you gifts...etc.

Industry/Entity Type

It Company

Colors

Designer to choose colors to be used in the design.

Requirements
Must have
• We are looking for a simple, cute and elegant gift card that reflects our branding. Must be customizable and printable on a standard printer.
• Must be single-sided 5x7.

```html
<!DOCTYPE html>
<html lang="en">
<head>
<meta charset="utf-8">
<title>The Merry Pantry – Gift Note Card</title>
<link rel="stylesheet" href="https://fonts.googleapis.com/css2?family=Source+Sans+3:wght@400;600&display=swap">
<style>
  :root {
    --backdrop: #b1b1b1;
    --brand-red: #8e0000;
    --brand-red-soft: #9b1515;
    --paper: #ffffff;
    --ink: #0d0f10;
    --quote-text: #f4f4f4;
    --muted-text: rgba(255, 255, 255, 0.72);
  }
  html, body {
    margin: 0;
    padding: 0;
    width: 857px;
    height: 1200px;
    overflow: hidden;
    background: var(--backdrop);
  }
  .canvas {
    position: relative;
    width: 857px;
    height: 1200px;
    background: var(--backdrop);
  }
  .note-card {
    position: absolute;
    left: 162px;
    top: 226px;
    width: 533px;
    height: 748px;
    background: var(--brand-red);
    font-family: "Source Sans 3", "Myriad Pro", sans-serif;
  }
  .band {
    position: absolute;
    left: 0;
    width: 100%;
  }
  .band--logo {
    top: 76px;
    height: 203px;
    background: var(--paper);
    display: flex;
    align-items: center;
    justify-content: center;
    gap: 16px;
  }
  .brand-mark {
    width: 30px;
    height: 30px;
    border-radius: 50%;
    background: var(--brand-red);
  }
  .brand-name {
    font-weight: 600;
    font-size: 42px;
    color: var(--ink);
    letter-spacing: 0.5px;
  }
  .gift-message {
    position: absolute;
    left: 46px;
    top: 306px;
    width: 441px;
    height: 196px;
    border-radius: 14px;
    background: var(--brand-red-soft);
  }
  .band--quote {
    top: 525px;
    height: 111px;
    background: var(--ink);
    display: flex;
    align-items: center;
    justify-content: center;
  }
  .quote {
    margin: 0;
    font-weight: 600;
    font-size: 18.5px;
    line-height: 25px;
    color: var(--quote-text);
    text-align: center;
  }
  .quote__author {
    display: block;
  }
  .website {
    position: absolute;
    left: 0;
    top: 636px;
    width: 100%;
    height: 112px;
    margin: 0;
    display: flex;
    align-items: center;
    justify-content: center;
    font-weight: 400;
    font-size: 15px;
    letter-spacing: 0.6px;
    color: var(--muted-text);
  }
</style>
</head>
<body>
  <div class="canvas">
    <section class="note-card">
      <div class="band band--logo">
        <span class="brand-mark" aria-hidden="true"></span>
        <span class="brand-name">The Merry Pantry</span>
      </div>
      <div class="gift-message" role="img" aria-label="Space for the customer's personal gift message"></div>
      <div class="band band--quote">
        <p class="quote">
          Food is symbolic of love when words are inadequate.
          <span class="quote__author">—Brent K. Hollister</span>
        </p>
      </div>
      <p class="website">themerrypantrybites.com</p>
    </section>
  </div>
</body>
</html>
```